i need a business card for a plumbing company in california

we are a drain cleaning , maintenance plumbing company who is starting new marketing campaign for a tatrench-less pipe installation department .

the professional who appreciates time and quality workmanship.

Plumbing

0655a3
ec1f27

• the second logo needs to be included
• a focus on the services offered
• any underlined words on the brief

```html
<!DOCTYPE html>
<html lang="en">
<head>
<meta charset="utf-8">
<title>Clearline Plumbing – Business Card</title>
<link rel="stylesheet" href="https://fonts.googleapis.com/css2?family=Open+Sans:wght@400;600;700;800&display=swap">
<style>
  :root {
    --backdrop: #ebebeb;
    --paper: #ffffff;
    --red: #f2545b;
    --red-deep: #d8323a;
    --grey: #9d9a92;
    --grey-dark: #7b7870;
    --ink-light: #e7e5e0;
  }
  * { margin: 0; padding: 0; box-sizing: border-box; }
  html, body {
    width: 1200px;
    height: 1066px;
    overflow: hidden;
    background: var(--backdrop);
    font-family: "Open Sans", sans-serif;
  }
  .sheet {
    width: 1200px;
    height: 1066px;
    display: flex;
    flex-direction: column;
    align-items: center;
    justify-content: center;
    gap: 70px;
  }
  .card {
    width: 560px;
    height: 320px;
    display: block;
    background: var(--paper);
    box-shadow: 0 10px 30px rgba(0,0,0,0.12);
  }
  .company-name { font-weight: 800; font-size: 26px; fill: var(--red); letter-spacing: 1px; font-family: "Open Sans", sans-serif; }
  .company-services { font-weight: 400; font-size: 10px; fill: var(--ink-light); letter-spacing: 2.5px; font-family: "Open Sans", sans-serif; }
  .contact-text { font-weight: 600; font-size: 11px; fill: var(--red); letter-spacing: 1px; font-family: "Open Sans", sans-serif; }
  .icon-box { fill: var(--red-deep); }
  .icon-line { fill: none; stroke: #fff; stroke-width: 1.4; stroke-linecap: round; stroke-linejoin: round; }
  .brand-name { font-weight: 700; font-size: 40px; fill: var(--grey); font-family: "Open Sans", sans-serif; }
</style>
</head>
<body>
<main class="sheet">

  <svg class="card card-back" viewBox="0 0 560 320" aria-label="Business card, contact side">
    <rect width="560" height="320" fill="var(--paper)"/>
    <path class="accent-thin" d="M0,188 C160,170 330,90 560,62" fill="none" stroke="var(--grey)" stroke-width="6"/>
    <path class="accent-red" d="M0,160 C160,142 330,62 560,34 L560,52 C330,78 160,158 0,178 Z" fill="var(--red)"/>
    <path class="top-band" d="M0,0 H560 V36 C330,62 160,140 0,158 Z" fill="var(--grey-dark)"/>
    <path class="corner-red" d="M0,0 H70 C50,14 20,22 0,24 Z" fill="var(--red-deep)"/>

    <text class="company-name" x="28" y="64">COMPANY</text>
    <text class="company-services" x="30" y="88">DRAIN CLEANING · TRENCHLESS PIPE</text>

    <g class="contact-list" text-anchor="end">
      <g class="contact-item" transform="translate(508,150)">
        <rect class="icon-box" width="24" height="24"/>
        <path class="icon-line" d="M8,6 l3,0 l1,4 l-2,1 q1,3 4,4 l1,-2 l4,1 l0,3 q-9,1 -11,-11 z"/>
        <text class="contact-text" x="-12" y="9">+0000 0000 000</text>
        <text class="contact-text" x="-12" y="23">+2222 2222 222</text>
      </g>
      <g class="contact-item" transform="translate(508,188)">
        <rect class="icon-box" width="24" height="24"/>
        <circle class="icon-line" cx="12" cy="12" r="7"/>
        <path class="icon-line" d="M5,12 h14 M12,5 q-4,7 0,14 M12,5 q4,7 0,14"/>
        <text class="contact-text" x="-12" y="16">WWW.@EXAMPLE.COM</text>
      </g>
      <g class="contact-item" transform="translate(508,224)">
        <rect class="icon-box" width="24" height="24"/>
        <rect class="icon-line" x="5" y="7" width="14" height="10"/>
        <path class="icon-line" d="M5,7 l7,6 l7,-6"/>
        <text class="contact-text" x="-12" y="16">MAIL@EXAMPLE.COM</text>
      </g>
      <g class="contact-item" transform="translate(508,260)">
        <rect class="icon-box" width="24" height="24"/>
        <circle class="icon-line" cx="12" cy="10" r="3"/>
        <path class="icon-line" d="M12,19 q-6,-6 -5,-10 a5,5 0 0 1 10,0 q1,4 -5,10 z"/>
        <text class="contact-text" x="-12" y="16">COMPANY.COM</text>
      </g>
    </g>
  </svg>

  <svg class="card card-front" viewBox="0 0 560 320" aria-label="Business card, brand side">
    <defs>
      <clipPath id="card-edge"><rect width="560" height="320"/></clipPath>
    </defs>
    <g clip-path="url(#card-edge)">
      <rect width="560" height="320" fill="var(--red)"/>
      <ellipse class="grey-arc" cx="280" cy="160" rx="300" ry="232" fill="var(--grey)"/>
      <ellipse class="white-field" cx="280" cy="160" rx="284" ry="222" fill="var(--paper)"/>
    </g>
    <g class="brand-lockup">
      <rect class="brand-mark" x="148" y="128" width="40" height="40" fill="var(--red)"/>
      <text class="brand-name" x="204" y="150">Clearline</text>
      <text class="brand-name" x="204" y="192">Plumbing</text>
    </g>
  </svg>

</main>
</body>
</html>
```